Business Card Design Project

We are a distribution company providing goods to Latin America. We sell everything from Medical equipment, generic medicines, to carecliners. The logo that we use is attached. The logo can incorporate different colors other than black for versatility. The company name is Valdren Global Enterprises and/or VGE. The card will be printed using 1 or more of the following: Silk mounted and/or embossed. So if the design ideas could be made to incorporate that technique or any other unique techniques, it would be great. The target market is dialysis centers/doctors.

Basic Info for card:
Marna Dowell
Purchasing Manager
417-305-6184 direct
417-521-7790 fax
marna.dowell@valdrenvge.example
www.valdrenvge.example

Target Market(s)

Latin America

Industry/Entity Type

Business

Requirements
Nice to have
• The Front of the card should have the basic contact information with company name/logo. The back of the card could incorporate

```html
<!DOCTYPE html>
<html lang="en">
<head>
<meta charset="utf-8">
<title>Valdren Global Enterprises — Business Card</title>
<link rel="stylesheet" href="https://fonts.googleapis.com/css2?family=Oswald:wght@600&display=swap">
<style>
  :root {
    --ink: #000000;
    --paper: #ffffff;
    --edge: #d9d9d9;
    --stripe-dark: #6e6e6e;
    --stripe-light: #c4c4c4;
  }
  html, body {
    margin: 0;
    padding: 0;
    width: 1200px;
    height: 901px;
    overflow: hidden;
    background: var(--paper);
  }
  .sheet { display: block; width: 1200px; height: 901px; }
  .brand-text {
    font-family: "Oswald", "Arial Narrow", sans-serif;
    font-weight: 600;
  }
  .front-name { font-size: 72px; fill: var(--ink); }
  .back-name { font-size: 17px; fill: var(--ink); }
  .back-mark-name { font-size: 30px; fill: var(--paper); }
  .holder-name { font-size: 19px; fill: var(--paper); }
  .holder-title { font-size: 14px; fill: var(--paper); }
  .contact-line { font-size: 16px; fill: var(--paper); }
  .card-edge { fill: var(--paper); stroke: var(--edge); stroke-width: 1; }
  .ink-fill { fill: var(--ink); }
</style>
</head>
<body>
<svg class="sheet" viewBox="0 0 1200 901" xmlns="http://www.w3.org/2000/svg">
  <defs>
    <linearGradient id="stripe-fade" x1="0" y1="0" x2="0" y2="1">
      <stop offset="0" stop-color="var(--stripe-dark)"/>
      <stop offset="0.6" stop-color="var(--stripe-light)"/>
      <stop offset="0.62" stop-color="#ffffff"/>
      <stop offset="1" stop-color="#ffffff"/>
    </linearGradient>
  </defs>

  <g class="card-front">
    <rect class="card-edge" x="369" y="152" width="513" height="289"/>
    <circle class="ink-fill" cx="630" cy="262" r="78"/>
    <text class="brand-text front-name" x="630" y="412" text-anchor="middle">Valdren</text>
    <rect class="ink-fill front-band" x="369" y="427" width="513" height="14"/>
  </g>

  <g class="card-back">
    <rect class="card-edge" x="369" y="483" width="513" height="290"/>
    <polygon class="ink-fill back-slab" points="571,483 882,483 882,773 369,773"/>
    <polygon class="back-stripe" points="722,483 763,483 641,658 605,658" fill="url(#stripe-fade)"/>
    <polygon class="back-stripe" points="882,535 882,592 834,658 798,658" fill="url(#stripe-fade)"/>

    <text class="brand-text back-name" x="386" y="563">Valdren</text>

    <text class="brand-text back-mark-name" x="818" y="718" text-anchor="middle">VGE</text>

    <g class="holder-block">
      <text class="brand-text holder-name" x="482" y="626">Marna Dowell</text>
      <text class="brand-text holder-title" x="482" y="646">Purchasing Manager</text>
    </g>

    <g class="contact-block">
      <text class="brand-text contact-line" x="530" y="697">417-305-6184 direct</text>
      <text class="brand-text contact-line" x="530" y="720">417-521-7790 fax</text>
      <text class="brand-text contact-line" x="530" y="741">www.valdrenvge.example</text>
      <text class="brand-text contact-line" x="530" y="762">marna.dowell@valdrenvge.example</text>
    </g>
  </g>
</svg>
</body>
</html>
```